Cedar Grove Steward Book Cover and Back Design

DESIGN BRIEF: The Cedar Grove Steward Book Cover
Author: Mayor Bernard T. Hale
Title: The Cedar Grove Steward
Subtitle: Raising Builders that shape neighbourhoods
Genre: Leadership / Personal Development / Public Service
Format: Paperback + eBook + Hardcover
Design a visually compelling, iconic book cover that captures the essence of authentic, legacy-driven leadership using the metaphor of the mango tree. The cover should be vibrant, symbolic, and memorable—something that could stand alone as a brand and invite both credibility and curiosity.
Cover should NOT include:
Author’s face or personal photo
Overly busy visuals or political imagery
Literal images of mayors, buildings, or people
Cover SHOULD include:
A single iconic mango tree or mango fruit with visible deep roots
A vibrant and rich color palette—think mango orange, deep green, warm gold, and earth tones
A design that feels both modern and timeless, with symbolic depth
A sense of growth, depth, and legacy
Room for bold typography that pops in print and thumbnails
🖼️ VISUAL CONCEPT IDEAS
(Designer may interpret creatively, but these are preferred themes.)
A stylized mango tree with glowing mangoes and roots extending downward, set against a vibrant background (sunrise or rich green sky)
A mango fruit icon with leaves and roots subtly worked into the shape — could be used across brand platforms
Optional: Split background showing transformation — one side dry/cracked earth, the other lush and fruitful
Clean, modern layout with breathing space and balance between image and title
✍️ TYPOGRAPHY
Title Font: Strong, elegant serif or modern classic (e.g., Playfair Display, Garamond, or Libre Baskerville)
Subtitle Font: Clean and crisp sans serif (e.g., Lato, Montserrat)
Author Name: Bold, uppercase — not oversized, but clearly legible
🔠 COPY FOR COVER
Title:
The Cedar Grove Steward
Subtitle:
Raising Builders That Shape Neighbourhoods
Author Name:
Mayor Bernard T. Hale
Optional Tagline or Teaser (for back or spine):
Stop performing like a politician. Start producing like a leader.
🔧 FORMAT DELIVERABLES
Front cover (paperback and hardcover versions)
Spine and back cover layout (with placeholder for barcode and description)
Web-optimized version for Borvix PDP and other retailers
Square version for social media promotion
Optional: Icon version of tree or mango for branding
Back of book: Are you tired of leadership that looks impressive but produces no lasting fruit?
In a culture obsessed with image over integrity, quick wins over deep roots, and self-promotion over public service, we need a new kind of leader—one who leads for legacy, not likes.
What if you stopped leading like an apple tree—and started leading like a mango tree?
Apple trees grow fast and look good for a season, but their shallow roots can’t weather the storms. Mango trees grow slowly, but they last for generations—producing sweet, lasting fruit long after their planter is gone.
This isn’t just a metaphor. It’s a mindset shift. And it’s the key to leadership that actually transforms people, places, and policy.
Mayor Bernard Hale has spent over a decade turning Dumfries, Virginia, from a town people drove through into a town people now drive to. Under his leadership:
• A former landfill became a half-billion-dollar resort
• A forgotten town rediscovered its purpose• A generation of young people began to see public service as purpose, not performance
In The Cedar Grove Steward, you’ll discover how to:
✅ Lead from your authentic strengths—not trends or titles✅ Identify the unique problem you were born to solve✅ Build coalitions rooted in trust, not transaction✅ Make decisions that create sustainable change✅ Develop future leaders who multiply your impact✅ Leave a legacy that grows long after you’re gone
Whether you’re an elected official, aspiring public servant, nonprofit founder, or community-builder, this book will help you lead like a tree: planted deeply, growing steadily, and bearing fruit that feeds others for generations.
Stop performing like a politician. Start producing like a leader.Plant deep. Lead strong. Leave fruit that lasts.
By the time you finish this book, you won’t just understand the mango tree model—you’ll own it. You’ll walk away with clarity, courage, and a roadmap to become the kind of leader your community needs and your future demands.
Leadership

```html
<!DOCTYPE html>
<html lang="en">
<head>
<meta charset="utf-8">
<title>The Cedar Grove Steward — Front Cover</title>
<link href="https://fonts.googleapis.com/css2?family=Bebas+Neue&family=Open+Sans:wght@700;800&family=Oswald:wght@500&family=Playfair+Display:ital@1&display=swap" rel="stylesheet">
<style>
  :root {
    --backdrop: #e9e7e3;
    --paper: #ffffff;
    --mango: #d95e19;
    --leaf: #328a42;
    --ink: #0d0d0d;
    --canopy-light: #8cc152;
    --canopy-deep: #2f7a38;
    --trunk: #7a5a3f;
  }
  * { margin: 0; padding: 0; box-sizing: border-box; }
  html, body {
    width: 1200px; height: 1200px; overflow: hidden;
    background: var(--backdrop);
  }
  .stage {
    width: 1200px; height: 1200px;
    display: flex; align-items: center; justify-content: center;
  }
  .cover {
    position: relative;
    width: 776px; height: 1165px;
    background: var(--paper);
    overflow: hidden;
  }
  .tree-art {
    position: absolute;
    left: 117px; top: 18px;
    width: 541px; height: 523px;
    border-radius: 48% 48% 30% 30% / 55% 55% 20% 20%;
    background:
      radial-gradient(ellipse 70% 60% at 50% 40%, var(--canopy-light), var(--canopy-deep) 75%, rgba(47,122,56,0) 100%),
      linear-gradient(to bottom, transparent 70%, var(--trunk) 100%);
  }
  .article-row {
    position: absolute;
    left: 52px; right: 52px; top: 540px;
    height: 90px;
    display: flex; align-items: center; justify-content: space-between;
  }
  .rule { width: 240px; height: 14px; display: block; }
  .article {
    font-family: "Playfair Display", "Times New Roman", serif;
    font-style: italic;
    font-size: 92px;
    line-height: 1;
    color: var(--ink);
  }
  .title-main {
    position: absolute;
    left: 0; right: 0; top: 612px;
    text-align: center;
    font-family: "Bebas Neue", "Oswald", sans-serif;
    font-size: 322px;
    line-height: 1;
    color: var(--mango);
    white-space: nowrap;
  }
  .title-sub {
    position: absolute;
    left: 0; right: 0; top: 858px;
    text-align: center;
    font-family: "Bebas Neue", "Oswald", sans-serif;
    font-size: 136px;
    line-height: 1;
    color: var(--leaf);
    white-space: nowrap;
  }
  .subtitle {
    position: absolute;
    left: 0; right: 0; top: 1000px;
    text-align: center;
    font-family: "Open Sans", Arial, sans-serif;
    font-weight: 800;
    font-size: 39px;
    line-height: 48px;
    color: var(--ink);
    text-transform: uppercase;
    letter-spacing: 0.01em;
  }
  .author-band {
    position: absolute;
    left: 0; right: 0; bottom: 0;
    height: 51px;
    background: var(--mango);
    display: flex; align-items: center; justify-content: center;
  }
  .author {
    font-family: "Oswald", Arial, sans-serif;
    font-weight: 500;
    font-size: 30px;
    letter-spacing: 0.18em;
    color: var(--paper);
    text-transform: uppercase;
  }
</style>
</head>
<body>
<main class="stage">
  <article class="cover">
    <div class="tree-art" role="img" aria-label="Watercolour illustration of a leafy mango tree heavy with green and orange mangoes, standing on a patch of earth"></div>

    <div class="article-row">
      <svg class="rule" viewBox="0 0 240 14" aria-hidden="true">
        <polygon points="0,7 240,0 240,14" fill="var(--ink)"/>
      </svg>
      <span class="article">The</span>
      <svg class="rule" viewBox="0 0 240 14" aria-hidden="true">
        <polygon points="0,0 240,7 0,14" fill="var(--ink)"/>
      </svg>
    </div>

    <h1 class="title-main">CEDAR</h1>
    <p class="title-sub">GROVE STEWARD</p>

    <p class="subtitle">Raising Builders That<br>Shape Neighbourhoods</p>

    <footer class="author-band">
      <span class="author">Mayor Bernard T. Hale</span>
    </footer>
  </article>
</main>
</body>
</html>
```